Redesign of Real Estate Agency Website

We need a redesign for our real estate agency website. Please see attached creative brief.

Target Market(s)

Refer to creative brief.

Industry/Entity Type

Real Estate

Requirements
Must have
• Refer to creative brief.

```html
<!DOCTYPE html>
<html lang="en">
<head>
<meta charset="utf-8">
<title>Shoreline Keys – Phuket Property and Real Estate for Sale</title>
<link href="https://fonts.googleapis.com/css2?family=Didact+Gothic&display=swap" rel="stylesheet">
<style>
:root{
  --page-bg:#e6e6e6;
  --page-light:#f7f7f7;
  --ink:#333333;
  --ink-soft:#444444;
  --accent:#1a8fd6;
  --accent-red:#d42a2a;
  --panel-top:#ffffff;
  --panel-bottom:#d9d9d9;
  --map-box:#c4c4c4;
  --field-line:#b9b9b9;
  --select-end:#8fd9f3;
}
*{margin:0;padding:0;box-sizing:border-box}
html,body{width:1200px;height:980px;overflow:hidden}
body{
  font-family:"Didact Gothic",sans-serif;
  color:var(--ink);
  background:radial-gradient(ellipse 700px 600px at 560px 470px,var(--page-light),var(--page-bg) 75%,#d2d2d2);
  position:relative;
}
.abs{position:absolute}
.brand{left:240px;top:104px;font-size:25px;color:#1d4f8f;letter-spacing:.3px}
.brand-tagline{left:367px;top:128px;font-size:8.5px;color:var(--ink)}
.main-nav a{position:absolute;top:167px;font-size:12.5px;color:var(--ink);text-decoration:none}
.main-nav a.current{color:var(--accent)}
.hero-panel{left:228px;top:198px;width:754px;height:233px;border-radius:9px;
  background:linear-gradient(180deg,var(--panel-top) 0%,#efefef 55%,var(--panel-bottom) 100%);
  box-shadow:2px 3px 6px rgba(0,0,0,.35)}
.hero-title{font-size:14px;color:var(--accent);top:223px}
.hero-photo{box-shadow:4px 4px 5px rgba(0,0,0,.45)}
.photo-condo{left:263px;top:255px;width:238px;height:151px;background:linear-gradient(160deg,#cfd6da 0%,#6fb3d4 45%,#2d8fb8 70%,#8c7a63 100%)}
.photo-villa{left:542px;top:251px;width:245px;height:153px;background:linear-gradient(180deg,#e9eef2 0%,#7a5a42 45%,#c98a4a 70%,#6b4a38 100%)}
.region-select{left:811px;top:251px;width:158px;height:19px;border:1px solid var(--field-line);
  background:linear-gradient(90deg,#fff 0%,#eef7fb 60%,var(--select-end) 100%);font-size:10px;padding:3px 6px}
.region-arrows{position:absolute;right:0;top:0;width:18px;height:17px;background:#4ec3ee}
.search-field{left:850px;top:283px;width:119px;height:19px;border:1px solid var(--field-line);border-radius:10px;background:#fff}
.search-field svg{position:absolute;right:7px;top:4px}
.intro-title{left:244px;top:453px;font-size:14.5px;color:var(--accent-red)}
.intro-text{left:244px;top:477px;width:420px;font-size:11.6px;line-height:15.3px;color:var(--ink-soft)}
.browse-title{left:790px;top:449px;font-size:18px;color:var(--accent)}
.browse-list{left:790px;top:477px;list-style:none;font-size:13.5px;line-height:21.3px;color:var(--ink)}
.map-box{left:779px;top:622px;width:202px;height:257px;border-radius:8px;background:var(--map-box)}
.map-title{left:791px;top:630px;font-size:17px;color:var(--accent)}
.map-option{top:659px;font-size:13.5px;color:var(--ink-soft);display:flex;align-items:center;gap:9px}
.map-area{left:800px;top:697px;width:157px;height:157px;background:linear-gradient(135deg,#dfe6e2,#b8bfbc 60%,#cdd6d1);box-shadow:1px 2px 3px rgba(0,0,0,.3)}
.topic{width:190px}
.topic h3{font-weight:normal;font-size:12.2px;color:var(--accent);margin-bottom:4px}
.topic p{font-size:9.6px;line-height:12.6px;color:var(--ink)}
</style>
</head>
<body>
  <div class="abs brand">Shoreline Keys</div>
  <div class="abs brand-tagline">Phuket Property and Real Estate for Sale</div>

  <nav class="main-nav">
    <a style="left:241px">Home</a>
    <a class="current" style="left:311px">Property For Sale</a>
    <a style="left:452px">Contact Us</a>
    <a style="left:556px">About Us</a>
    <a style="left:662px">List Your Property</a>
    <a style="left:802px">Property Buyer's Guide</a>
  </nav>

  <div class="abs hero-panel"></div>
  <div class="abs hero-title" style="left:260px">Apartments &amp; Condos For Sale</div>
  <div class="abs hero-title" style="left:542px">Villas &amp; Houses For Sale</div>
  <div class="abs hero-photo photo-condo" role="img" aria-label="Photo of a sea view apartment with pool"></div>
  <div class="abs hero-photo photo-villa" role="img" aria-label="Photo of a lit tropical villa at dusk"></div>
  <div class="abs region-select">Region
    <span class="region-arrows"><svg width="18" height="17"><path d="M6 7l3-3 3 3zM6 10l3 3 3-3z" fill="#1d4f8f"/></svg></span>
  </div>
  <div class="abs search-field"><svg width="11" height="11"><circle cx="6.5" cy="4.5" r="3" fill="none" stroke="#888" stroke-width="1.3"/><path d="M4.3 6.7L1 10" stroke="#888" stroke-width="1.8"/></svg></div>

  <h1 class="abs intro-title" style="font-weight:normal">Shoreline Keys Real Estate Agents</h1>
  <p class="abs intro-text">Whether you are searching for a beachfront villa, sea view apartment or an exciting investment opportunity we can help you find your ideal Phuket property. We have selected the finest properties that Phuket has to offer. Our highly experienced sales team is available to provide further details on any Phuket property for sale and we would be delighted to arrange viewings. Please contact us with your Phuket real estate requirements.</p>

  <h2 class="abs browse-title" style="font-weight:normal">Browse Property for Sale</h2>
  <ul class="abs browse-list">
    <li>Hot Properties &amp; Promotions</li>
    <li>Apartments &amp; Condos</li>
    <li>Villas &amp; Houses</li>
    <li>Land</li>
    <li>Commercial</li>
    <li>Property Buyer's Guide</li>
  </ul>

  <div class="abs map-box"></div>
  <div class="abs map-title">Search By Map</div>
  <div class="abs map-option" style="left:795px"><svg width="14" height="14"><circle cx="7" cy="7" r="6" fill="#f4f4f4" stroke="#666"/><circle cx="7" cy="7" r="3" fill="#5a9a5a"/></svg>Buy</div>
  <div class="abs map-option" style="left:869px"><svg width="14" height="14"><circle cx="7" cy="7" r="6" fill="#f4f4f4" stroke="#666"/></svg>Rent</div>
  <div class="abs map-area" role="img" aria-label="Map of Phuket island with property locations"></div>

  <section class="abs topic" style="left:243px;top:620px">
    <h3>Why Buy Property in Phuket?</h3>
    <p>There is an excellent choice of properties on the island to suit every budget with excellent capital appreciation and strong rental returns... more</p>
  </section>
  <section class="abs topic" style="left:247px;top:709px">
    <h3>Foreign Ownership</h3>
    <p>Foreign nationals and juristic entities are prohibited from owning land under Thai law. However, there are a number of options available... more</p>
  </section>
  <section class="abs topic" style="left:247px;top:805px">
    <h3>Property FAQ</h3>
    <p>Frequently asked questions about Phuket property for sale... more</p>
  </section>
  <section class="abs topic" style="left:488px;top:619px">
    <h3>Land Titles</h3>
    <p>When buying Phuket real estate it is imperative to be aware of the type of title deed of the land plot... more</p>
  </section>
  <section class="abs topic" style="left:488px;top:704px">
    <h3>Land Units</h3>
    <p>- 1 Rai = 4 Ngan (1,600 sqm)<br>- 1 Ngan = 100 square Wah (400 sqm)<br>- 1 square Wah = 4 sqm... more</p>
  </section>
  <section class="abs topic" style="left:489px;top:800px">
    <h3>Property Taxes &amp; Fees</h3>
    <p>When a property in Thailand is purchased or sold there are four potential taxes/fees to be paid. Which of these taxes/fees will be applicable depends on the details of the transaction... more</p>
  </section>
</body>
</html>
```